Window cleaning and Pressure washing

Truck wrap partial or full/background:
Would like to see a background of a water mark or something related to window cleaning. And or pressure washing.

Doors of the truck:
Need to have my logo printed in big on the doors and with LLC in small after the logo. Need to have my slogan below my logo on the door.
Slogan is; “Affordable 5 star services!”

Sides of the truck:
Want to see window cleaning and Pressure washing on the sides of the truck in big letters with the phone number. Slanted with a shadow effect.
(Would like to see slanted and not slanted) also need to see something that signifies 100% satisfaction or your money back!Preferably a sticker, Or a combination of both. Also need to have residential and commercial somewhere.
Phone number needs to be on here.

Tailgate:
Want to have the services on the back tailgate with the slogan, as well as the 100% money back guarantee sticker.
And the phone number here to!

Back window;
Needs to have the same background as the wrap on the truck or very slimier with the water swiped away Clean with the logo presented as shown in one of the pictures below.

```html
<!DOCTYPE html>
<html lang="en">
<head>
<meta charset="utf-8">
<title>The Bright Mile LLC — Truck Wrap</title>
<link rel="stylesheet" href="https://fonts.googleapis.com/css2?family=Anton&family=Montserrat:wght@600;700&display=swap">
<style>
  :root {
    --wrap-blue: #1b87d6;
    --wrap-blue-deep: #0d5fb8;
    --wrap-cyan: #08a9ef;
    --accent-orange: #fbab0b;
    --badge-dark: #2b2b2b;
    --white: #ffffff;
    --emblem-gold: #d9a520;
    --chrome-edge: #2a2a2a;
  }
  html, body {
    margin: 0;
    padding: 0;
    width: 1056px;
    height: 1200px;
    overflow: hidden;
    background: var(--white);
  }
  .wrap-sheet { display: block; width: 1056px; height: 1200px; }
  .body-fill { fill: var(--wrap-blue); }
  .cutout { fill: var(--white); }
  .deep-panel { fill: var(--wrap-blue-deep); opacity: .55; }
  .orange { fill: var(--accent-orange); }
  .cyan { fill: var(--wrap-cyan); }
  .white { fill: var(--white); }
  .dark { fill: var(--badge-dark); }

  .ui-text { font-family: "Montserrat", sans-serif; font-weight: 700; fill: var(--white); }
  .ui-text.semibold { font-weight: 600; }
  .ui-text.blue { fill: var(--wrap-blue); }
  .brand-name { font-family: "Montserrat", sans-serif; font-weight: 700; fill: var(--white); }
  .chrome-text {
    font-family: "Anton", sans-serif;
    fill: url(#chrome);
    stroke: var(--chrome-edge);
    stroke-width: 1.5;
    paint-order: stroke;
  }
  .guarantee-pct { font-family: "Anton", sans-serif; fill: var(--accent-orange); stroke: #b86f00; stroke-width: 1; paint-order: stroke; }
  .guarantee-line { font-family: "Anton", sans-serif; fill: var(--white); }
  .guarantee-line.dark-ink { fill: var(--badge-dark); }
  .stars { fill: #ffd21a; font-family: "Montserrat", sans-serif; }
  .vehicle-emblem { font-family: "Montserrat", sans-serif; font-weight: 700; fill: var(--emblem-gold); }
  .tick-ring { fill: var(--white); stroke: var(--accent-orange); stroke-width: 4; }
  .tick { fill: none; stroke: var(--accent-orange); stroke-width: 4; stroke-linecap: round; stroke-linejoin: round; }
  .phone-icon { fill: none; stroke: var(--white); stroke-linecap: round; stroke-linejoin: round; }
</style>
</head>
<body>
<svg class="wrap-sheet" viewBox="0 0 1800 2045" xmlns="http://www.w3.org/2000/svg">
  <defs>
    <linearGradient id="chrome" x1="0" y1="0" x2="0" y2="1">
      <stop offset="0" stop-color="#ffffff"/>
      <stop offset=".55" stop-color="#e4e4e4"/>
      <stop offset="1" stop-color="#9a9a9a"/>
    </linearGradient>
    <linearGradient id="bodyShade" x1="0" y1="0" x2="0" y2="1">
      <stop offset="0" stop-color="#2192df"/>
      <stop offset="1" stop-color="#1479cc"/>
    </linearGradient>
    <linearGradient id="affordableBand" x1="0" y1="0" x2="1" y2="0">
      <stop offset="0" stop-color="#fbab0b" stop-opacity="0"/>
      <stop offset=".3" stop-color="#fbab0b"/>
      <stop offset="1" stop-color="#fbab0b"/>
    </linearGradient>
    <linearGradient id="starBand" x1="0" y1="0" x2="1" y2="0">
      <stop offset="0" stop-color="#08a9ef"/>
      <stop offset=".8" stop-color="#08a9ef"/>
      <stop offset="1" stop-color="#08a9ef" stop-opacity="0"/>
    </linearGradient>
    <linearGradient id="silverBand" x1="0" y1="0" x2="1" y2="1">
      <stop offset="0" stop-color="#8c8c8c"/>
      <stop offset=".5" stop-color="#f2f2f2"/>
      <stop offset="1" stop-color="#7a7a7a"/>
    </linearGradient>
    <linearGradient id="cleanWindowScene" x1="0" y1="0" x2="1" y2="1">
      <stop offset="0" stop-color="#9fb3c4"/>
      <stop offset=".45" stop-color="#7d8a8c"/>
      <stop offset=".75" stop-color="#9cc07a"/>
      <stop offset="1" stop-color="#eef3f3"/>
    </linearGradient>
    <clipPath id="rearWindowShape">
      <path d="M270,1768 L340,1440 Q350,1420 420,1410 Q700,1380 1000,1388 Q1200,1392 1320,1410 Q1340,1420 1345,1440 L1402,1768 Z"/>
    </clipPath>
  </defs>

  <!-- ===== Side panel ===== -->
  <g class="side-panel">
    <path fill="url(#bodyShade)" d="M205,395 L215,375 Q300,350 515,330 L560,330 Q590,320 640,280 L730,210 Q760,195 940,188 Q965,190 970,215 L985,335 L1590,328 L1595,365 L1560,370 L1545,475 L1590,480 L1590,500 L1545,505 L1540,585 L1435,592 L1430,480 Q1420,440 1300,440 Q1180,440 1170,480 L1160,582 L565,592 L545,500 Q530,440 420,435 Q315,430 300,470 L298,475 L275,476 L278,395 Z"/>
    <path class="cutout" d="M625,345 L640,330 Q700,260 870,205 L895,205 Q910,210 910,230 L908,345 L665,355 Q630,358 625,345 Z"/>
    <rect class="cutout" x="830" y="388" width="82" height="14" rx="7"/>
    <path class="deep-panel" d="M880,335 L1130,335 L1090,590 L880,590 L912,468 Z"/>

    <g class="credentials">
      <text class="ui-text semibold" x="330" y="383" font-size="24">LICENSED AND</text>
      <rect class="orange" x="330" y="390" width="182" height="27"/>
      <text class="ui-text" x="421" y="412" font-size="22" letter-spacing="6" text-anchor="middle">INSURED</text>
    </g>

    <g class="door-brand">
      <text class="brand-name" x="605" y="406" font-size="42">THE</text>
      <text class="brand-name" x="605" y="456" font-size="48">BRIGHT</text>
      <text class="brand-name" x="672" y="490" font-size="40">MILE <tspan font-size="20">LLC</tspan></text>
    </g>

    <path fill="url(#affordableBand)" d="M545,500 L850,500 L862,537 L560,537 Z"/>
    <text class="ui-text" x="612" y="531" font-size="32">AFFORDABLE</text>
    <path fill="url(#starBand)" d="M590,540 L1070,540 L1090,580 L605,580 Z"/>
    <text class="ui-text" x="625" y="572" font-size="34">5 STAR SERVICES!</text>

    <g class="service-headline">
      <text class="chrome-text" x="928" y="393" font-size="46">WINDOW</text>
      <text class="chrome-text" x="928" y="438" font-size="46">CLEANING AND</text>
      <text class="chrome-text" x="928" y="484" font-size="46">PRESSURE</text>
      <text class="chrome-text" x="928" y="530" font-size="46">WASHING</text>
    </g>

    <path class="orange" d="M1135,335 L1590,328 L1595,365 L1548,370 L1544,398 L1170,398 Z"/>
    <g class="phone-badge">
      <circle cx="1157" cy="365" r="23" fill="#1b87d6" stroke="#fff" stroke-width="3"/>
      <path class="phone-icon" stroke-width="4" d="M1150,352 q-6,3 -2,14 q5,11 14,12 l4,-5"/>
    </g>
    <text class="chrome-text" x="1198" y="388" font-size="52">(555) 014-2290</text>
    <rect class="white" x="1228" y="396" width="280" height="28"/>
    <text class="ui-text blue" x="1368" y="417" font-size="18" text-anchor="middle">Commercial &amp; Residential</text>

    <g class="guarantee-sticker small">
      <text class="guarantee-pct" x="1490" y="475" font-size="40" text-anchor="middle">100%</text>
      <rect class="dark" x="1443" y="480" width="94" height="30" rx="4"/>
      <text class="guarantee-line" x="1490" y="493" font-size="10" text-anchor="middle">SATISFACTION OR</text>
      <rect class="white" x="1450" y="496" width="80" height="10"/>
      <text class="guarantee-line dark-ink" x="1490" y="504" font-size="8" text-anchor="middle">YOUR MONEY BACK!</text>
      <text class="stars" x="1490" y="526" font-size="12" text-anchor="middle" letter-spacing="3">★★★★★</text>
      <text class="ui-text semibold" x="1490" y="549" font-size="10" text-anchor="middle">Follow Us</text>
      <circle class="white" cx="1477" cy="565" r="8"/>
      <circle class="white" cx="1502" cy="565" r="8"/>
    </g>
  </g>

  <!-- ===== Tailgate ===== -->
  <g class="tailgate">
    <path fill="url(#bodyShade)" d="M340,728 L365,728 L370,778 L1438,778 L1442,732 L1465,732 L1468,1025 L1468,1158 L338,1158 L333,1025 Z"/>
    <path class="cutout" d="M812,795 L993,795 Q1006,797 1004,812 L995,872 Q990,887 975,887 L830,887 Q815,887 811,872 L800,812 Q799,797 812,795 Z"/>

    <g class="services-list">
      <circle class="tick-ring" cx="404" cy="833" r="17"/><path class="tick" d="M396,833 l6,6 l11,-11"/>
      <text class="chrome-text" x="438" y="852" font-size="44">WINDOW CLEANING</text>
      <circle class="tick-ring" cx="404" cy="897" r="17"/><path class="tick" d="M396,897 l6,6 l11,-11"/>
      <text class="chrome-text" x="438" y="916" font-size="44">HOUSE WASHING</text>
      <circle class="tick-ring" cx="404" cy="961" r="17"/><path class="tick" d="M396,961 l6,6 l11,-11"/>
      <text class="chrome-text" x="438" y="980" font-size="44">PRESSURE WASHING</text>

      <circle class="tick-ring" cx="1068" cy="833" r="17"/><path class="tick" d="M1060,833 l6,6 l11,-11"/>
      <text class="chrome-text" x="1102" y="852" font-size="44">ROOF CLEANING</text>
      <circle class="tick-ring" cx="1068" cy="897" r="17"/><path class="tick" d="M1060,897 l6,6 l11,-11"/>
      <text class="chrome-text" x="1102" y="916" font-size="44">GUTTER CLEANING</text>
      <circle class="tick-ring" cx="1068" cy="961" r="17"/><path class="tick" d="M1060,961 l6,6 l11,-11"/>
      <text class="chrome-text" x="1102" y="980" font-size="44">SCREEN REPAIRS</text>
    </g>

    <text class="vehicle-emblem" x="902" y="955" font-size="24" text-anchor="middle">RIDGEWAY</text>

    <g class="phone-strip">
      <rect class="cyan" x="333" y="1025" width="160" height="133"/>
      <path class="orange" d="M380,1025 L1195,1025 L1262,1158 L475,1158 Z"/>
      <rect class="white" x="1262" y="1025" width="206" height="133"/>
      <path class="white" d="M1195,1025 L1262,1025 L1262,1158 Z"/>
      <circle class="orange" cx="424" cy="1088" r="42" stroke="#fff" stroke-width="6"/>
      <path class="phone-icon" stroke-width="7" d="M412,1064 q-12,6 -3,28 q10,22 26,22 l7,-9"/>
      <text class="chrome-text" x="508" y="1130" font-size="100">(555) 014-2290</text>
    </g>

    <g class="guarantee-sticker large">
      <text class="guarantee-pct" x="1340" y="1050" font-size="66" text-anchor="middle">100%</text>
      <path class="cyan" d="M1275,1100 L1410,1100 L1400,1115 L1285,1115 Z"/>
      <rect class="dark" x="1262" y="1053" width="158" height="52" rx="10"/>
      <text class="guarantee-line" x="1341" y="1076" font-size="19" text-anchor="middle">SATISFACTION OR</text>
      <rect class="white" x="1272" y="1080" width="138" height="19"/>
      <text class="guarantee-line dark-ink" x="1341" y="1096" font-size="16" text-anchor="middle">YOUR MONEY BACK!</text>
      <text class="stars" x="1341" y="1136" font-size="22" text-anchor="middle" letter-spacing="4">★★★★★</text>
    </g>
  </g>

  <!-- ===== Rear window ===== -->
  <g class="rear-window" clip-path="url(#rearWindowShape)">
    <rect x="260" y="1380" width="1150" height="400" fill="url(#bodyShade)"/>
    <path fill="url(#silverBand)" d="M1010,1385 L1082,1385 L792,1770 L702,1770 Z"/>
    <path fill="url(#cleanWindowScene)" d="M1082,1385 L1410,1385 L1410,1770 L792,1770 Z"
          role="img" aria-label="Photo of a gloved hand squeegeeing a soapy window, a house blurred behind it"/>
    <g class="rear-brand">
      <text class="brand-name" x="390" y="1542" font-size="74">THE</text>
      <text class="brand-name" x="418" y="1626" font-size="86">BRIGHT</text>
      <text class="brand-name" x="515" y="1690" font-size="74">MILE</text>
    </g>
  </g>
</svg>
</body>
</html>
```